Kestrel Cove Camp

We need a web page that details location/distance to Melbourne, the facilities available, the magnificent setting, contact information, history of the area and our background in the industry booking enquiry page linked to our email account, feedback page.
(Refer www.campbrindlepoint.com.au for details and further imagary as we operate in the same facility and Camp Brindle Point Business no longer exists) WE WANT A BETTER WEBSITE THAN THIS!!

```html
<!DOCTYPE html>
<html lang="en">
<head>
<meta charset="utf-8">
<title>Kestrel Cove Camp</title>
<link href="https://fonts.googleapis.com/css2?family=Open+Sans:wght@400;600;700&display=swap" rel="stylesheet">
<style>
:root{
  --header:#231714;
  --blue:#1b8fd6;
  --blue-dark:#0f6fb3;
  --blue-text:#1a88c9;
  --orange:#f08a0c;
  --text:#777;
  --line:#e3e3e3;
  --band:#f3f3f3;
  --footer:#2c2c2c;
}
*{margin:0;padding:0;box-sizing:border-box}
html,body{width:789px;height:1200px;overflow:hidden;background:#fff}
body{font-family:"Open Sans",Arial,sans-serif;color:var(--text);position:relative}
.abs{position:absolute}

.site-header{left:0;top:0;width:789px;height:126px;background:var(--header)}
.brand{left:66px;top:64px;display:flex;align-items:center;gap:8px}
.brand-dot{width:30px;height:30px;border-radius:50%;background:var(--orange)}
.brand-name{color:var(--orange);font-weight:700;font-size:19px;white-space:nowrap}
.social{right:66px;top:29px;display:flex;gap:6px}
.social span{width:21px;height:21px;border-radius:50%}
.contact-call{left:376px;top:72px;text-align:right;width:120px;white-space:nowrap}
.contact-call small,.contact-dir small{display:block;color:#ddd;font-size:10px}
.contact-call strong,.contact-dir strong{display:block;color:var(--blue-text);font-weight:400;font-size:15px;line-height:18px}
.contact-dir{left:530px;top:72px;text-align:right;width:165px;white-space:nowrap}

.main-nav{left:0;top:126px;width:789px;height:35px;background:linear-gradient(#2a9ae0,#1482cb)}
.main-nav ul{list-style:none;display:flex;position:absolute;left:66px;top:0;height:35px;border-left:1px solid #0f6fb3}
.main-nav li{height:35px;line-height:35px;color:#fff;font-size:11px;padding:0 17px;border-right:1px solid #0f6fb3;white-space:nowrap}
.main-nav li.active{background:var(--blue-dark);padding:0 21px}

.hero{left:0;top:161px;width:789px;height:311px;background:linear-gradient(170deg,#b9cde0 0%,#4a82a8 12%,#1f6f9f 35%,#2f8fbd 60%,#9fb790 78%,#5f7f48 100%)}
.hero-caption{left:0;top:415px;width:789px;height:57px;background:rgba(20,25,30,.55)}
.hero-caption h2{position:absolute;left:88px;top:10px;color:#fff;font-weight:400;font-size:14px;white-space:nowrap}
.hero-caption p{position:absolute;left:88px;top:32px;color:#eee;font-size:8.4px;white-space:nowrap}

h2.section{color:var(--blue-text);font-weight:400;font-size:15px;white-space:nowrap}
p.body{font-size:8.3px;line-height:14.5px}

.video{left:564px;top:504px;width:158px;height:89px;border:2px solid #222;background:linear-gradient(#5b7fa5 0%,#93a9bc 45%,#c8b89b 70%,#a89a7c 100%)}
.play{left:67px;top:29px;width:27px;height:27px}

.rule{left:66px;width:658px;height:1px;background:var(--line)}

.facility{width:149px;top:677px}
.facility .photo{height:84px}
.facility h3{color:var(--orange);font-weight:400;font-size:10px;margin-top:8px;white-space:nowrap}
.facility p{font-size:8.3px;line-height:13px;margin-top:3px}

.event{left:564px;width:158px;height:36px;background:#eee;display:flex}
.event .date{width:31px;background:var(--orange);color:#fff;text-align:center;padding-top:4px;flex:none}
.event .date small{display:block;font-size:6px}
.event .date b{display:block;font-weight:400;font-size:13px;line-height:14px}
.event p{font-size:8.3px;line-height:11.5px;padding:6px 4px 0 9px}

.contact-band{left:0;top:1074px;width:789px;height:63px;background:var(--band)}
.contact-item{top:0;height:63px;display:flex;align-items:center;gap:10px;font-size:8.3px;line-height:15px;white-space:nowrap}
.site-footer{left:0;top:1137px;width:789px;height:63px;background:var(--footer)}
.footer-links{left:66px;top:17px;font-size:8px;color:#ddd;word-spacing:1px;white-space:nowrap}
.copyright{left:66px;top:41px;font-size:8px;color:#ccc;white-space:nowrap}
.footer-social{right:66px;top:25px;display:flex;gap:5px}
.footer-social span{width:17px;height:17px;border-radius:50%;background:#666}
</style>
</head>
<body>

<header class="site-header abs">
  <div class="brand abs"><span class="brand-dot"></span><span class="brand-name">Kestrel Cove Camp</span></div>
  <div class="social abs">
    <span style="background:#3b5998"></span><span style="background:#1da1f2"></span><span style="background:#555"></span>
    <span style="background:#e02a2a"></span><span style="background:#f57d00"></span><span style="background:#e52d27"></span>
    <span style="background:#5a7ea8"></span><span style="background:#6ab04c"></span>
  </div>
  <div class="contact-call abs"><small>Call us</small><strong>654 208 3917</strong></div>
  <svg class="abs" style="left:500px;top:74px" width="25" height="25" viewBox="0 0 25 25"><circle cx="12.5" cy="12.5" r="11" fill="none" stroke="#ddd" stroke-width="1.5"/><path d="M9 7c-1 1-1 3 1 6s4 5 6 5l1.5-1.5-2-2-1.3 1c-1-.5-2.5-2-3-3l1-1.3-2-2z" fill="#ddd"/></svg>
  <div class="contact-dir abs"><small>55, Street name, City - Zip code</small><strong>Get Directions</strong></div>
  <svg class="abs" style="left:699px;top:74px" width="25" height="25" viewBox="0 0 25 25"><circle cx="12.5" cy="12.5" r="11" fill="none" stroke="#ddd" stroke-width="1.5"/><path d="M12.5 6a4 4 0 0 0-4 4c0 3 4 8 4 8s4-5 4-8a4 4 0 0 0-4-4z" fill="none" stroke="#ddd" stroke-width="1.4"/><circle cx="12.5" cy="10" r="1.3" fill="#ddd"/></svg>
</header>

<nav class="main-nav abs">
  <ul>
    <li class="active">HOME</li><li>ABOUT US</li><li>ACCOMODAION</li><li>EVENTS</li><li>CAMPS</li><li>OUR LOCATION</li><li>CONTACT US</li>
  </ul>
</nav>

<section class="hero abs" role="img" aria-label="Aerial photograph of a curved sandy bay with blue water and green farmland"></section>
<div class="hero-caption abs">
  <h2>Praesent consectetur lacus</h2>
  <p>Cum sociis natoque penatibus et magnis dis parturient montes, nascetur ridiculus mus.</p>
  <svg class="abs" style="left:20px;top:20px" width="12" height="18"><path d="M10 1 2 9l8 8" fill="none" stroke="#bbb" stroke-width="2"/></svg>
  <svg class="abs" style="left:756px;top:20px" width="12" height="18"><path d="M2 1l8 8-8 8" fill="none" stroke="#bbb" stroke-width="2"/></svg>
</div>

<section class="welcome">
  <h2 class="section abs" style="left:67px;top:497px">Welcome to Kestrel Cove Camp</h2>
  <p class="body abs" style="left:67px;top:524px;width:482px">Nam sit amet elit quis risus sagittis efficitur. Pellentesque dignissim, ante at commodo tempor, lacus quam vestibulum justo, eget faucibus sapien purus sit amet est. Phasellus elit eros, lobortis id commodo non, ultricies elementum purus. Pellentesque in mauris at leo hendrerit tempus. Lorem ipsum dolor sit amet, consectetur adipiscing elit. Etiam et lectus mi. Donec pretium urna quis egestas luctus. Nulla et facilisis nulla, vel consectetur ipsum. Nullam rutrum quis lectus ac dignissim.&nbsp; Sed et dui sagittis, lobortis leo sit amet, hendrerit tortor.</p>
  <div class="video abs" role="img" aria-label="Video still of a wide empty beach at low tide">
    <svg class="play abs" viewBox="0 0 27 27"><circle cx="13.5" cy="13.5" r="13" fill="#e8e8e8"/><path d="M11 8l8 5.5-8 5.5z" fill="#555"/></svg>
  </div>
</section>

<div class="rule abs" style="top:624px"></div>

<section class="facilities">
  <h2 class="section abs" style="left:66px;top:641px">Facilities Available</h2>
  <svg class="abs" style="left:536px;top:646px" width="11" height="11"><circle cx="5.5" cy="5.5" r="5.5" fill="#ccc"/><path d="M4.5 3l2.5 2.5L4.5 8" fill="none" stroke="#fff" stroke-width="1.3"/></svg>
  <div class="facility abs" style="left:67px">
    <div class="photo" role="img" aria-label="Photograph of a campfire on the beach at dusk" style="background:linear-gradient(#7b8fb0,#3d4f73 55%,#2a3350)"></div>
    <h3>Praesent quis nisl turpis</h3>
    <p>Nullam rutrum quis lectus ac dignissim.&nbsp; Sed et dui sagittis, lobortis leo sit amet, hendrerit tortor.</p>
  </div>
  <div class="facility abs" style="left:233px">
    <div class="photo" role="img" aria-label="Photograph of food cooking on a round barbecue grill" style="background:linear-gradient(#d8d2c8,#7c7168 55%,#3a3431)"></div>
    <h3>Praesent quis nisl turpis</h3>
    <p>Nullam rutrum quis lectus ac dignissim.&nbsp; Sed et dui sagittis, lobortis leo sit amet, hendrerit tortor.</p>
  </div>
  <div class="facility abs" style="left:399px">
    <div class="photo" role="img" aria-label="Photograph of thatched umbrellas and sun loungers on a beach" style="background:linear-gradient(#7fb3e0,#c9dff0 50%,#e5d9c3)"></div>
    <h3>Praesent quis nisl turpis</h3>
    <p>Nullam rutrum quis lectus ac dignissim.&nbsp; Sed et dui sagittis, lobortis leo sit amet, hendrerit tortor.</p>
  </div>
</section>

<aside class="events">
  <h2 class="section abs" style="left:563px;top:641px">Events</h2>
  <div class="event abs" style="top:677px"><div class="date"><small>Aug</small><b>31</b></div><p>Sed et dui sagittis, lobortis leo sit amet, hendrerit</p></div>
  <div class="event abs" style="top:718px"><div class="date"><small>Aug</small><b>31</b></div><p>Sed et dui sagittis, lobortis leo sit amet, hendrerit</p></div>
  <div class="event abs" style="top:760px"><div class="date"><small>Aug</small><b>31</b></div><p>Sed et dui sagittis, lobortis leo sit amet, hendrerit</p></div>
  <div class="abs" style="left:565px;top:808px;font-size:8.5px;color:var(--blue-text)">VIEW ALL</div>
</aside>

<div class="rule abs" style="top:857px"></div>

<section class="history">
  <div class="abs" role="img" aria-label="Photograph of clear turquoise water beside a rocky headland and jetty" style="left:66px;top:885px;width:119px;height:163px;background:linear-gradient(#9fc6d9,#3fa6bd 40%,#2b8d9b)"></div>
  <h2 class="section abs" style="left:199px;top:885px">History of the Area</h2>
  <p class="body abs" style="left:200px;top:914px;width:392px;line-height:15.7px">Pellentesque eu iaculis leo. Aliquam erat volutpat. Sed et dui sagittis, lobortis leo sit amet, hendrerit tortor. Phasellus a neque eu enim posuere vulputate. Cras scelerisque lectus sit amet dolor fermentum, vitae dignissim sem rutrum.</p>
  <p class="body abs" style="left:200px;top:969px;width:392px;line-height:15.7px">Aliquam augue purus, commodo et dui ut, facilisis tempor mauris. Vivamus tempor in metus nec feugiat. Nullam cursus dolor fringilla, scelerisque arcu a, egestas massa. Suspendisse augue diam, consectetur at cursus sit amet, sodales volutpat sapien at imperdiet tellus. Etiam et lectus mi. Donec pretium urna quis egestas luctus. Nulla et facilisis nulla, vel consectetur ipsum. <span style="color:#b0261a">View Our Location&nbsp; ››</span></p>
  <div class="abs" style="left:599px;top:886px;font-size:8px;font-weight:700;color:#222">WHERE WE ARE</div>
  <div class="abs" role="img" aria-label="Location map showing the route from Melbourne to the camp on the coast" style="left:599px;top:900px;width:124px;height:154px;background:linear-gradient(135deg,#f6efe2 55%,#8fc1e3 56%)"></div>
</section>

<footer>
  <div class="contact-band abs">
    <div class="contact-item abs" style="left:74px">
      <svg width="15" height="18"><rect x="1" y="1" width="13" height="16" fill="none" stroke="#999" stroke-width="1.5"/><rect x="5" y="5" width="5" height="12" fill="#999"/></svg>
      <span>55, Building name, streetname<br>City - Zip code</span>
    </div>
    <div class="contact-item abs" style="left:253px">
      <svg width="20" height="20"><path d="M4 2c-2 2-2 6 2 11s8 6 10 5l2-2-3-3-2 1c-2-1-4-4-5-6l1-2-3-3z" fill="#999"/></svg>
      <span>Phone: 654 470 2815</span>
    </div>
    <div class="contact-item abs" style="left:400px">
      <svg width="19" height="18"><rect x="1" y="5" width="17" height="12" fill="none" stroke="#999" stroke-width="1.5"/><rect x="5" y="1" width="9" height="5" fill="#999"/></svg>
      <span>Fax : 465 390 7142</span>
    </div>
    <div class="contact-item abs" style="left:532px">
      <svg width="19" height="14"><rect x="1" y="1" width="17" height="12" fill="#999"/><path d="M1 1l8.5 7L18 1" fill="none" stroke="#f3f3f3" stroke-width="1.3"/></svg>
      <span>E-mail : info@kestrelcovecamp.com</span>
    </div>
  </div>
  <div class="site-footer abs">
    <div class="footer-links abs">Home&nbsp; | &nbsp;About us&nbsp; | &nbsp;Accomodaion&nbsp; | &nbsp;Events&nbsp; | &nbsp;Camps&nbsp; | &nbsp;Our Location&nbsp; | &nbsp;Contact us</div>
    <div class="copyright abs">Copyright &copy; 2014 Kestrel Cove Camp.&nbsp; All rights reserved.</div>
    <div class="footer-social abs"><span></span><span></span><span></span><span></span></div>
  </div>
</footer>

</body>
</html>
```